Service business needs Business Card Design

Looking to create a new business card design that is both professional and unique the can highlight the many services we offer throughout the seasons. Our tagline is "The Steadfast Touch"
Licensed & Insured: PA392617 has to be small and on the back side of the card.
On the Front:
FirstName LastName
Title
We offer the following services:
Deck Repair and Maintenance
Deck Cleaning and Staining/Painting
Power Washing/House Washing
Landscape Lighting Installation
Christmas Lighting Installation

```html
<!DOCTYPE html>
<html lang="en">
<head>
<meta charset="utf-8">
<title>Halden Services – Business Card</title>
<link rel="stylesheet" href="https://fonts.googleapis.com/css2?family=Lato:wght@400;700&family=Titillium+Web:wght@700&family=Chakra+Petch:wght@700&display=swap">
<style>
  :root {
    --page-bg: #2b2b2b;
    --card-white: #ffffff;
    --navy: #0a4f8f;
    --navy-deep: #03508f;
    --sky: #2aa7e0;
    --sky-light: #4fc6f0;
    --ink: #444444;
    --rule: #1d5a96;
  }
  * { margin: 0; padding: 0; box-sizing: border-box; }
  html, body { width: 1200px; height: 1200px; overflow: hidden; background: var(--page-bg); }
  .stage { position: relative; width: 1200px; height: 1200px; }

  .card {
    position: absolute; left: 281px; width: 638px; height: 366px;
    border-radius: 20px; overflow: hidden;
  }
  .card-front {
    top: 195px;
    background: linear-gradient(115deg, #e8f3fa 0%, #f4f8fb 40%, var(--card-white) 65%);
  }
  .card-back {
    top: 639px;
    background: var(--navy-deep);
  }

  .brand {
    position: absolute; right: 41px; top: 104px; text-align: right;
    font-family: "Titillium Web", sans-serif; font-weight: 700; color: var(--navy);
    display: flex; align-items: center; gap: 10px;
  }
  .brand-mark { width: 16px; height: 16px; border-radius: 50%; background: var(--navy); }
  .brand-name { font-size: 32px; line-height: 1; letter-spacing: 5px; }
  .brand-name small { display: block; font-size: 12px; letter-spacing: 11px; margin-top: 4px; }

  .holder { position: absolute; left: 37px; top: 142px; }
  .holder-name {
    font-family: "Titillium Web", sans-serif; font-weight: 700; font-size: 30px;
    line-height: 1; color: var(--navy); letter-spacing: .3px;
  }
  .holder-title {
    font-family: "Lato", sans-serif; font-size: 18px; color: var(--sky); margin-top: 3px;
  }
  .divider { position: absolute; left: 37px; right: 41px; top: 208px; height: 2px; background: var(--rule); }

  .contact {
    position: absolute; left: 35px; top: 222px; list-style: none;
    font-family: "Lato", sans-serif; font-size: 15px; color: var(--ink); line-height: 19.5px;
  }
  .contact li { display: flex; align-items: flex-start; gap: 10px; margin-bottom: 1px; }
  .contact li.address { margin-bottom: 5px; }
  .contact svg { width: 13px; height: 13px; margin-top: 3px; flex: none; fill: var(--sky); }

  .services {
    position: absolute; right: 41px; top: 222px; list-style: none; text-align: right;
    font-family: "Lato", sans-serif; font-size: 15.3px; color: var(--navy); line-height: 20px;
  }
  .services li { display: flex; justify-content: flex-end; align-items: center; gap: 9px; }
  .services svg { width: 12px; height: 12px; flex: none; }

  .footer-band { position: absolute; left: 0; right: 0; bottom: 0; height: 13px; display: flex; gap: 5px; }
  .footer-band .left { width: 358px; background: var(--navy); }
  .footer-band .right { flex: 1; background: linear-gradient(90deg, var(--sky) 0%, var(--navy) 100%); }

  .back-glow {
    position: absolute; inset: 0;
    background: radial-gradient(circle at 8% 15%, var(--sky-light) 0%, rgba(42,167,224,.55) 18%, rgba(3,80,143,0) 55%);
  }
  .tagline {
    position: absolute; right: 32px; top: 232px; text-align: right;
    font-family: "Chakra Petch", sans-serif; font-weight: 700; color: #fff;
    text-transform: uppercase; line-height: 1;
  }
  .tagline span { display: block; }
  .tagline .line-1 { font-size: 37px; letter-spacing: 1px; }
  .tagline .line-2 { font-size: 44px; letter-spacing: 1.5px; margin-top: 4px; }
  .license {
    position: absolute; left: 389px; top: 332px; font-family: "Lato", sans-serif;
    font-size: 11px; color: #fff; white-space: nowrap;
  }
</style>
</head>
<body>
<div class="stage">
  <section class="card card-front">
    <div class="brand">
      <span class="brand-mark"></span>
      <div class="brand-name">HALDEN<small>SERVICES</small></div>
    </div>

    <div class="holder">
      <div class="holder-name">MARC DELVANE</div>
      <div class="holder-title">Founder &amp; CEO</div>
    </div>
    <div class="divider"></div>

    <ul class="contact">
      <li class="address">
        <svg viewBox="0 0 24 24"><path d="M12 2a7 7 0 0 0-7 7c0 5 7 13 7 13s7-8 7-13a7 7 0 0 0-7-7zm0 9.5A2.5 2.5 0 1 1 12 6.5a2.5 2.5 0 0 1 0 5z"/></svg>
        <span>48 Meadowlark Lane,<br>Suite 204 Harlow, PA 19022</span>
      </li>
      <li>
        <svg viewBox="0 0 24 24"><path d="M6.6 10.8a15 15 0 0 0 6.6 6.6l2.2-2.2a1 1 0 0 1 1-.25 11.4 11.4 0 0 0 3.6.57 1 1 0 0 1 1 1V20a1 1 0 0 1-1 1A17 17 0 0 1 3 4a1 1 0 0 1 1-1h3.5a1 1 0 0 1 1 1c0 1.250.2 2.450.57 3.57a1 1 0 0 1-.25 1z"/></svg>
        <span>215.555.0148 Or 610.555.0193</span>
      </li>
      <li>
        <svg viewBox="0 0 24 24"><path d="M2 5h20v14H2zm2 2v.5l8 5 8-5V7l-8 5z"/></svg>
        <span>info@haldenservicesgroup.com</span>
      </li>
      <li>
        <svg viewBox="0 0 24 24"><path d="M12 2a10 10 0 1 0 0 20 10 10 0 0 0 0-20zm-1 17.9A8 8 0 0 1 4.2 10.6L9 15.4v1a2 2 0 0 0 2 2zm6.9-2.5A2 2 0 0 0 16 16h-1v-3a1 1 0 0 0-1-1H8v-2h2a1 1 0 0 0 1-1V7h2a2 2 0 0 0 2-2v-.4a8 8 0 0 1 2.9 12.8z"/></svg>
        <span>www.haldenservicesgroup.com</span>
      </li>
    </ul>

    <ul class="services">
      <li>Deck Repair &amp; Maintenance <svg viewBox="0 0 12 12"><circle cx="6" cy="6" r="6" fill="#2aa7e0"/><path d="M3.2 6.2l2 2 3.6-4" stroke="#fff" stroke-width="1.6" fill="none"/></svg></li>
      <li>Deck Cleaning &amp; Staining/Painting <svg viewBox="0 0 12 12"><circle cx="6" cy="6" r="6" fill="#2aa7e0"/><path d="M3.2 6.2l2 2 3.6-4" stroke="#fff" stroke-width="1.6" fill="none"/></svg></li>
      <li>Power Washing/House Washing <svg viewBox="0 0 12 12"><circle cx="6" cy="6" r="6" fill="#2aa7e0"/><path d="M3.2 6.2l2 2 3.6-4" stroke="#fff" stroke-width="1.6" fill="none"/></svg></li>
      <li>Landscape Lighting Installation <svg viewBox="0 0 12 12"><circle cx="6" cy="6" r="6" fill="#2aa7e0"/><path d="M3.2 6.2l2 2 3.6-4" stroke="#fff" stroke-width="1.6" fill="none"/></svg></li>
      <li>Christmas Lighting Installation <svg viewBox="0 0 12 12"><circle cx="6" cy="6" r="6" fill="#2aa7e0"/><path d="M3.2 6.2l2 2 3.6-4" stroke="#fff" stroke-width="1.6" fill="none"/></svg></li>
    </ul>

    <div class="footer-band"><div class="left"></div><div class="right"></div></div>
  </section>

  <section class="card card-back">
    <div class="back-glow" role="img" aria-label="Soft light-blue glow spreading from the top-left corner"></div>
    <h1 class="tagline"><span class="line-1">The Steadfast</span><span class="line-2">Touch</span></h1>
    <p class="license">Licensed &amp; Insured: PA392617</p>
  </section>
</div>
</body>
</html>
```